Mobile Optometry needs descriptive brochure and business cards for patients

I need a brochure design and business cards for a new optometry service that brings full ocular examination, refraction, and spectacle dispensing to the patient in need.
I will mainly be working out of senior homes so it needs to be very legible NO SMALL PRINT, CLEAR, CONSCIENCE.
The final design needs to incorporate the logo and colouring that was just selected from a previous project. I will add this file as soon as I get the final changes back from the designer.

Here is what I would like in the broacher. I don't have a fax number, website address, email address set up yet but have room for this.

Note: I have attached the logo I selected for the company. I may not have attached the most detailed version but this will give you an idea of colouring and style. I will upload the proper image soon.

Routine eye examinations are crucial for early detection of diseases of the eye and effects of systemic conditions for everybody. As we age we are at higher risk of vision loss due to Glaucoma, Age-related Macular Degeneration, Diabetic or Hypertensive Retinopathy, Cataracts and many other diseases.

During your complete ocular visual assessment you will be screened for all conditions that may be affecting you as well as treat any issues you may be suffering from. Common treatable complaints: Dry eyes, Watery eyes, Burning, Itching, Difficulty reading small print, Reduced distance vision, Glare, Light sensitiveness, and difficulty performing hobbies.

Here is what your complete examination includes

Step 1: Appointment Request
-Call
-Email
-Phone
-Fax

Step 2: Welcome form
-Patient Name, DOB, QR Wellcover number
-List current medications, allergies
-Current Visual difficulties
-Previous spectacle prescription (if available)

Step 3: Ocular Visual Assessment and Discussion of Results
-History & Symptoms
-Refraction
-Dilation and thorough ocular/retinal screening
-Spectacle or magnifier dispense if required
-Ophthalmologist or medical practitioner referral if required

Step 4: Dispense and Delivery
-Return to fit custom made glasses
-Demonstrate use low vision device
-Discuss any questions/treatments/referrals

I have just increased the budget. I am running out of time and want some good designs. I want a modern, clean and clear product. Please submit, points for originality.

Target Market(s)

The target audience is Professionals, managers, senior care facilities, families. I want something clean and easy to read. I want something modern but not trendy and something that appeals to the masses.

Industry/Entity Type

Medical

Font styles to use
Sans Serif

Requirements
Must have
• easy to read
bright
professional
Contact information on the last page
Nice to have
• order of services layer out nicely. Try a version with clearly defined steps. Step 1. Step 2. Step 3. Could be multiple broachers that are packaged together.
Should not have
• cartoony
serif fonts (please use font that is in logo)

```html
<!DOCTYPE html>
<html lang="en">
<head>
<meta charset="utf-8">
<title>Clear-View Eye Care – Brochure Inside Spread</title>
<link rel="stylesheet" href="https://fonts.googleapis.com/css2?family=Source+Sans+3:wght@400;600;700&display=swap">
<style>
  :root {
    --white: #ffffff;
    --ink: #2f2f31;
    --blue: #2ea3da;
    --blue-band: #36a3d9;
    --green: #7dbd3d;
    --teal: #1db79c;
    --slate: #6d6e71;
    --mist: #e6e7e8;
    --trim: #b9b9b9;
    --photo-light: #e9e4df;
    --photo-dark: #c9c1b9;
  }
  * { margin: 0; padding: 0; box-sizing: border-box; }
  html, body {
    width: 1200px; height: 811px; overflow: hidden;
    background: var(--white);
    font-family: "Source Sans 3", "Myriad Pro", Arial, sans-serif;
    color: var(--ink);
  }
  .canvas { width: 1200px; height: 811px; overflow: hidden; position: relative; }
  .spread {
    position: absolute; top: 0; left: 0;
    width: 1334px; height: 901px;
    transform: scale(0.8996); transform-origin: 0 0;
  }
  .artwork { position: absolute; inset: 0; }

  .block { position: absolute; }

  .brand { left: 397px; top: 158px; display: flex; align-items: center; gap: 10px; }
  .brand-dot { width: 16px; height: 16px; border-radius: 50%; background: var(--blue); }
  .brand-name { font-size: 25px; font-weight: 600; color: var(--slate); letter-spacing: -0.3px; }
  .brand-tag {
    left: 432px; top: 194px; font-size: 11px; letter-spacing: 0.6px; color: var(--ink);
  }

  .lead {
    left: 397px; top: 242px; width: 225px;
    font-size: 18px; line-height: 22.5px; color: var(--blue);
  }
  .intro {
    left: 726px; top: 107px; width: 225px;
    font-size: 18px; line-height: 22.5px; color: var(--ink);
  }
  .intro p + p { margin-top: 22px; }

  .complaints { left: 983px; top: 107px; width: 260px; }
  .complaints h2 {
    font-size: 24px; line-height: 24px; font-weight: 700; color: var(--teal);
    margin-bottom: 26px;
  }
  .complaints li { font-size: 18px; line-height: 24px; }

  ul { list-style: none; }
  .dot-list li { position: relative; padding-left: 10px; }
  .dot-list li::before {
    content: ""; position: absolute; left: 0; top: 0.62em;
    width: 4px; height: 4px; border-radius: 50%; background: var(--teal);
  }

  .includes {
    left: 96px; top: 478px; width: 140px;
    font-size: 18px; line-height: 20px; color: var(--white);
  }

  .step { top: 568px; }
  .step-label { font-size: 17px; line-height: 20px; color: var(--ink); }
  .step-title {
    font-size: 22px; line-height: 24px; color: var(--blue); font-weight: 400; margin-top: 4px;
  }
  .step-title strong { font-weight: 700; }
  .step .dot-list { margin-top: 12px; }
  .step .dot-list li { font-size: 15px; line-height: 20px; margin-bottom: 4px; }
  .step-1 { left: 268px; width: 150px; }
  .step-2 { left: 438px; width: 200px; }
  .step-3 { left: 726px; width: 230px; }
  .step-4 { left: 983px; width: 240px; }

  .size-note { left: 1187px; top: 879px; font-size: 10px; color: var(--ink); }
</style>
</head>
<body>
<div class="canvas">
  <div class="spread">
    <svg class="artwork" width="1334" height="901" viewBox="0 0 1334 901" aria-hidden="false">
      <defs>
        <linearGradient id="portraitTone" x1="0" y1="0" x2="1" y2="1">
          <stop offset="0" stop-color="var(--photo-light)"/>
          <stop offset="1" stop-color="var(--photo-dark)"/>
        </linearGradient>
        <clipPath id="trimArea"><rect x="46" y="0" width="1242" height="855"/></clipPath>
      </defs>

      <!-- trim marks -->
      <g class="trim-marks" stroke="var(--trim)" stroke-width="1">
        <line x1="0" y1="54" x2="36" y2="54"/><line x1="54" y1="0" x2="54" y2="36"/>
        <line x1="1298" y1="54" x2="1334" y2="54"/><line x1="1280" y1="0" x2="1280" y2="36"/>
        <line x1="0" y1="847" x2="36" y2="847"/><line x1="54" y1="865" x2="54" y2="901"/>
        <line x1="1298" y1="847" x2="1334" y2="847"/><line x1="1280" y1="865" x2="1280" y2="901"/>
        <line x1="667" y1="0" x2="667" y2="36" stroke-dasharray="3 3"/>
        <line x1="667" y1="865" x2="667" y2="901" stroke-dasharray="3 3"/>
      </g>

      <g clip-path="url(#trimArea)">
        <rect role="img" aria-label="Portrait photograph of a smiling senior woman wearing glasses"
              x="110" y="65" width="280" height="360" fill="url(#portraitTone)"/>
        <path class="band-green" d="M46,255 Q600,600 1288,335 L1288,855 L46,855 Z" fill="var(--green)"/>
        <path class="band-blue" d="M46,298 Q600,636 1288,345 L1288,855 L46,855 Z" fill="var(--blue-band)"/>
        <path class="band-gap" d="M46,400 Q620,680 1288,368 L1288,855 L46,855 Z" fill="var(--white)"/>
        <path class="panel-light" d="M46,408 Q620,688 1288,376 L1288,855 L46,855 Z" fill="var(--mist)"/>
        <path class="panel-dark" d="M46,408 Q160,466 278,496 Q140,620 46,800 Z" fill="var(--slate)"/>
      </g>

      <!-- arrow button -->
      <circle cx="116" cy="590" r="17" fill="none" stroke="var(--white)" stroke-width="2"/>
      <path d="M111,581 L120,590 L111,599" fill="none" stroke="var(--white)" stroke-width="2.5"/>

      <!-- step icons -->
      <g class="step-icon">
        <circle cx="300" cy="486" r="37" fill="var(--blue-band)" stroke="var(--white)" stroke-width="4"/>
        <circle cx="300" cy="486" r="19" fill="none" stroke="var(--white)" stroke-width="5"/>
        <path d="M300,475 L300,487 L309,492" fill="none" stroke="var(--white)" stroke-width="4" stroke-linecap="round"/>
      </g>
      <g class="step-icon">
        <circle cx="477" cy="513" r="37" fill="var(--blue-band)" stroke="var(--white)" stroke-width="4"/>
        <path d="M463,492 L484,492 L493,501 L493,533 L463,533 Z" fill="var(--white)"/>
        <g stroke="var(--blue-band)" stroke-width="2">
          <line x1="469" y1="508" x2="487" y2="508"/>
          <line x1="469" y1="515" x2="487" y2="515"/>
          <line x1="469" y1="522" x2="487" y2="522"/>
        </g>
      </g>
      <g class="step-icon">
        <circle cx="760" cy="521" r="37" fill="var(--blue-band)" stroke="var(--white)" stroke-width="4"/>
        <ellipse cx="760" cy="517" rx="22" ry="15" fill="var(--white)"/>
        <path d="M748,527 L744,540 L758,530 Z" fill="var(--white)"/>
      </g>
      <g class="step-icon">
        <circle cx="1017" cy="490" r="37" fill="var(--blue-band)" stroke="var(--white)" stroke-width="4"/>
        <path d="M998,491 L1017,473 L1036,491 L1031,491 L1031,506 L1021,506 L1021,496 L1013,496 L1013,506 L1003,506 L1003,491 Z" fill="var(--white)"/>
      </g>
    </svg>

    <div class="block brand">
      <span class="brand-dot"></span>
      <span class="brand-name">Clear-View Eye Care</span>
    </div>
    <div class="block brand-tag">MOBILE OPTOMETRY</div>

    <p class="block lead">Routine eye examinations are crucial for early signs of eye diseases and to ensure optimal vision with a current prescription.</p>

    <div class="block intro">
      <p>As we age the risk of vision loss due to Glaucoma, Age-related Macular Degeneration, Diabetic or Hypertensive Retinopathy, Cataracts and many other diseases.</p>
      <p>During your eye exam you will be screened for all eye conditions, ones that you may or may not be aware of.</p>
    </div>

    <div class="block complaints">
      <h2>Common treatable complaints:</h2>
      <ul class="dot-list">
        <li>Dry eyes</li>
        <li>Watery eyes</li>
        <li>Burning or Itching</li>
        <li>Difficulty reading small print</li>
        <li>Reduced distance vision</li>
        <li>Glare</li>
        <li>Light sensitiveness</li>
        <li>Difficulty performing</li>
        <li>Hobbies</li>
      </ul>
    </div>

    <p class="block includes">Here is what your complete examination includes:</p>

    <section class="block step step-1">
      <p class="step-label">Step 1</p>
      <h3 class="step-title"><strong>Appointment</strong><br>Request</h3>
      <ul class="dot-list">
        <li>Call</li><li>Email</li><li>Phone</li><li>Fax</li>
      </ul>
    </section>

    <section class="block step step-2">
      <p class="step-label">Step 2</p>
      <h3 class="step-title"><strong>Welcome</strong> form</h3>
      <ul class="dot-list">
        <li>Patient Name, DOB,<br>QR Wellcover number</li>
        <li>List current medications, allergies</li>
        <li>Current visual difficulties</li>
        <li>Previous spectacle prescription (if available)</li>
      </ul>
    </section>

    <section class="block step step-3">
      <p class="step-label">Step 3</p>
      <h3 class="step-title"><strong>Eye</strong> Exam</h3>
      <ul class="dot-list">
        <li>History &amp; Symptoms</li>
        <li>Determine current spectacle prescription</li>
        <li>Dilation and thorough ocular/retinal screening</li>
        <li>Select spectacle or magnifier</li>
        <li>Ophthalmologist or medical practitioner referral if required</li>
      </ul>
    </section>

    <section class="block step step-4">
      <p class="step-label">Step 4</p>
      <h3 class="step-title"><strong>Delivery</strong> of glasses</h3>
      <ul class="dot-list">
        <li>Second visit to bring new prescription glasses and ensure proper fit</li>
        <li>Demonstrate use<br>low vision device</li>
        <li>Discuss any<br>questions / treatments / referrals</li>
      </ul>
    </section>

    <p class="block size-note">17" x 11" B_SIDE</p>
  </div>
</div>
</body>
</html>
```